Commercial facility maintenance

I need a card design that helps my salesmen make contact with new clients, our product is facility maintenance and heavy industrial maintenance

```html
<!DOCTYPE html>
<html lang="en">
<head>
<meta charset="UTF-8">
<title>Harlow Millwrights LLC – Business Card</title>
<link rel="stylesheet" href="https://fonts.googleapis.com/css2?family=Montserrat:wght@400;500;700&display=swap">
<style>
  :root {
    --backdrop: #3b3b3d;
    --card: #121212;
    --white: #ffffff;
    --red: #a3212b;
    --text-light: #f2f2f2;
    --rule: #8e1d25;
  }
  * { margin: 0; padding: 0; box-sizing: border-box; }
  html, body { width: 1200px; height: 689px; overflow: hidden; }
  body {
    background: var(--backdrop);
    font-family: "Montserrat", Arial, sans-serif;
    position: relative;
  }
  .card {
    position: absolute;
    top: 196px;
    width: 520px;
    height: 297px;
    background: var(--card);
    border-radius: 22px;
    overflow: hidden;
  }
  .card--front { left: 50px; }
  .card--back { left: 630px; }

  /* Front */
  .brand-name {
    position: absolute;
    left: 0; right: 0; top: 92px;
    text-align: center;
    color: var(--text-light);
    font-weight: 700;
    font-size: 30px;
    letter-spacing: 1px;
  }
  .brand-name .mark {
    display: inline-block;
    width: 18px; height: 18px;
    border-radius: 50%;
    background: var(--text-light);
    margin-right: 12px;
    vertical-align: 2px;
  }
  .services-heading {
    position: absolute;
    left: 50px; right: 50px; top: 170px;
    display: flex; align-items: center; gap: 12px;
    color: var(--red);
    font-weight: 700;
    font-size: 17px;
  }
  .services-heading::before,
  .services-heading::after {
    content: ""; flex: 1; height: 1.5px; background: var(--rule);
  }
  .services-list {
    position: absolute;
    left: 0; right: 0; top: 206px;
    display: flex; justify-content: center; gap: 16px;
    list-style: none;
    color: var(--text-light);
    font-size: 14px;
  }
  .services-list li::before {
    content: "";
    display: inline-block;
    width: 8px; height: 8px; border-radius: 50%;
    background: var(--red);
    margin-right: 7px; vertical-align: 1px;
  }

  /* Back */
  .brand-panel {
    position: absolute;
    right: -20px; top: -40px;
    width: 290px; height: 290px;
    background: var(--white);
    border-radius: 50% 50% 50% 50% / 50% 50% 50% 50%;
    display: flex; align-items: center; justify-content: center;
  }
  .brand-panel .brand-panel-name {
    color: var(--red);
    font-weight: 700;
    font-size: 22px;
    text-align: center;
    line-height: 1.2;
    width: 180px;
    margin-right: 10px;
    margin-top: 30px;
  }
  .person {
    position: absolute;
    left: 36px; top: 70px;
  }
  .person-name {
    color: var(--red);
    font-weight: 700;
    font-size: 27px;
  }
  .person-role {
    color: var(--text-light);
    font-size: 13px;
    margin-top: 2px;
  }
  .contact {
    position: absolute;
    left: 36px; bottom: 34px;
    list-style: none;
    color: var(--text-light);
    font-size: 13.5px;
  }
  .contact li { display: flex; align-items: center; gap: 9px; margin-top: 6px; }
  .contact svg { width: 13px; height: 13px; fill: var(--red); flex: none; }
</style>
</head>
<body>

<section class="card card--front">
  <p class="brand-name"><span class="mark"></span>HARLOW MILLWRIGHTS LLC</p>
  <h2 class="services-heading">Services</h2>
  <ul class="services-list">
    <li>Facility Maintenance</li>
    <li>Heavy Industrial Maintenance</li>
  </ul>
</section>

<section class="card card--back">
  <div class="brand-panel">
    <p class="brand-panel-name">HARLOW MILLWRIGHTS LLC</p>
  </div>
  <div class="person">
    <h1 class="person-name">Daniel Harlow</h1>
    <p class="person-role">Owner</p>
  </div>
  <ul class="contact">
    <li>
      <svg viewBox="0 0 16 16" aria-hidden="true"><path d="M3.6 1.5l2.3 2.7-1.3 1.6c.9 2 2.5 3.6 4.6 4.6l1.6-1.3 2.7 2.3-1.3 2.4C6.8 13.6 2.4 9.2 1.2 2.8z"/></svg>
      555-014-2287
    </li>
    <li>
      <svg viewBox="0 0 16 16" aria-hidden="true"><path d="M1 3h14v10H1z M1.8 3.8L8 8.6l6.2-4.8" stroke="#121212" stroke-width="1"/></svg>
      dharlow@mailbox.example
    </li>
    <li>
      <svg viewBox="0 0 16 16" aria-hidden="true"><circle cx="8" cy="8" r="7"/><path d="M1 8h14M8 1c-3 3.5-3 10.5 0 14M8 1c3 3.5 3 10.5 0 14" stroke="#121212" stroke-width="1" fill="none"/></svg>
      harlowmillwrightsllc.example
    </li>
  </ul>
</section>

</body>
</html>
```